Visitenkarten mit schwarzem Design gesucht
Zielgruppe
Zielgruppe sind Feinschmecker & Genießer.
Aufgabenstellung
Front schwarz mit unserem goldenen Logo. Rückseite auch in schwarz mit Firmenname, Adresse, Telefon, Email und Webadresse.
Es wäre klasse, wenn nach Beendigung des Projektes Datei für drei Ansprechpartner zur Verfügung gestellt werden. Das heißt, drei verschiedene Namen und Telefonnummern. Der Rest wäre dann gleichbleibend.
Bei der Gestaltung bitte bei der .eps Datei nur das Logo verwenden und nicht den Text!

```html
<!DOCTYPE html>
<html lang="de">
<head>
<meta charset="utf-8">
<title>Gaumen &amp; Gourmet – Visitenkarten</title>
<link href="https://fonts.googleapis.com/css2?family=Lato:wght@400;700;900&display=swap" rel="stylesheet">
<style>
  :root {
    --bg: #141414;
    --card: #1d1d1d;
    --card-edge: #2a2a2a;
    --gold: #d4b25e;
    --gold-light: #f2dc94;
    --gold-dark: #a8873a;
    --white: #f4f4f4;
    --grey: #cfcfcf;
    --ink: #1a1a1a;
  }
  * { margin: 0; padding: 0; box-sizing: border-box; }
  html, body { width: 1200px; height: 912px; overflow: hidden; }
  body {
    background: var(--bg);
    font-family: "Lato", sans-serif;
    position: relative;
  }
  .card {
    position: absolute;
    width: 560px;
    height: 320px;
    background: var(--card);
    border: 1px solid var(--card-edge);
    box-shadow: 0 18px 40px rgba(0,0,0,.55);
    overflow: hidden;
  }
  .card--front { left: 70px; top: 90px; }
  .card--back  { left: 570px; top: 500px; }

  /* Front */
  .brand {
    position: absolute;
    left: 0; right: 0; top: 110px;
    display: flex; align-items: center; justify-content: center; gap: 14px;
  }
  .brand__dot {
    width: 16px; height: 16px; border-radius: 50%;
    background: var(--gold);
  }
  .brand__name {
    font-weight: 900;
    font-size: 40px;
    letter-spacing: .5px;
    color: var(--gold);
  }
  .front__web {
    position: absolute;
    left: 0; right: 0; bottom: 34px;
    text-align: center;
    font-size: 17px;
    color: var(--white);
    letter-spacing: .3px;
  }

  /* Back */
  .contact {
    position: absolute;
    left: 250px; top: 36px;
    color: var(--white);
  }
  .contact__name {
    font-weight: 900;
    font-size: 22px;
    color: var(--gold);
    line-height: 1.1;
  }
  .contact__role {
    font-size: 15px;
    color: var(--grey);
    margin: 3px 0 14px;
  }
  .contact__row {
    display: flex; gap: 9px;
    font-size: 15px;
    line-height: 1.3;
    margin-bottom: 10px;
  }
  .contact__icon { width: 14px; height: 16px; flex: none; margin-top: 2px; }
  .back__band {
    position: absolute; left: 0; bottom: 0;
    width: 560px; height: 120px;
  }
  .back__web {
    position: absolute;
    left: 26px; bottom: 8px;
    font-size: 17px;
    font-weight: 700;
    line-height: 20px;
    color: var(--ink);
  }
</style>
</head>
<body>

<section class="card card--front" aria-label="Vorderseite">
  <div class="brand">
    <span class="brand__dot"></span>
    <span class="brand__name">Gaumen &amp; Gourmet</span>
  </div>
  <p class="front__web">www.gaumenundgourmet.de</p>
</section>

<section class="card card--back" aria-label="Rückseite">
  <div class="contact">
    <p class="contact__name">Lukas Brenner</p>
    <p class="contact__role">Geschäftsführer</p>
    <div class="contact__row">
      <svg class="contact__icon" viewBox="0 0 14 16"><path d="M7 0a5.5 5.5 0 0 0-5.5 5.5C1.5 9.5 7 16 7 16s5.5-6.5 5.5-10.5A5.5 5.5 0 0 0 7 0zm0 7.6a2.1 2.1 0 1 1 0-4.2 2.1 2.1 0 0 1 0 4.2z" fill="var(--gold)"/></svg>
      <span>Gaumen &amp; Gourmet<br>Lindenhof-Straße 17<br>50733 Köln</span>
    </div>
    <div class="contact__row">
      <svg class="contact__icon" viewBox="0 0 14 16"><path d="M3 2l2.2 2.8-1.3 1.5c.8 1.8 2.2 3.2 4 4l1.5-1.3L12.2 11l-1.4 2.2C6 13 1 8 1 3.4z" fill="var(--gold)"/></svg>
      <span>+49 (0) 221 - 58 27 30 16</span>
    </div>
    <div class="contact__row">
      <svg class="contact__icon" viewBox="0 0 14 16"><rect x="0.5" y="3.5" width="13" height="9" fill="var(--gold)"/><path d="M0.5 3.5L7 9l6.5-5.5" stroke="#1d1d1d" stroke-width="1.2" fill="none"/></svg>
      <span>info@gaumenundgourmet.de</span>
    </div>
  </div>

  <svg class="back__band" viewBox="0 0 560 120" aria-hidden="true">
    <defs>
      <linearGradient id="bandGold" x1="0" y1="0" x2="1" y2="0">
        <stop offset="0" stop-color="var(--gold-dark)"/>
        <stop offset=".45" stop-color="var(--gold-light)"/>
        <stop offset="1" stop-color="var(--gold)"/>
      </linearGradient>
    </defs>
    <path d="M0 120 L0 86 C200 86 400 70 560 40 L560 120 Z" fill="url(#bandGold)"/>
    <path d="M330 120 C430 108 510 92 560 78 L560 120 Z" fill="var(--card)"/>
    <path d="M180 85 C350 80 470 56 560 20 L560 32 C460 64 340 82 180 86 Z" fill="#ffffff"/>
  </svg>
  <p class="back__web">www.gaumenundgourmet.de</p>
</section>

</body>
</html>
```